Systems and Technology Consultants - Website

Design & Build a website for a new company which operates in the Systems and Technology space for Transportation, Government and Commercial sectors.

Overall design should be minimalist in nature.
Should also have a feed that provides news and event updates on the main page.
Logo has already been awarded and should be incorporated into the site.

We like the overall layout, functionality and simplicity of the below sites. Submitted designs could be similar to or a combination of the aspects on these sites, or perhaps a whole different concept - we are open to new ideas.
Vortrane.com
Merp.it

Update 1 Dated 27 May 2014

All I am moving away from the Merp.it website and would like it to be more aligned with Vortrane.com not only in layout but in functionality. I will be extending the deadline of this design brief for two weeks to incorporate additional requirements and will add addtional funding to the project.

Apologies for not having more information available to provide but with so many submissions its getting confusing.

Thanks Dermot
Updates

Please note that the brief has been updated and the deadline has been extended.

Important: We will need two language versions of the website, English and Arabic; the website is hosted on HostPeak

Hello All, Thank you for your submissions. We have narrowed it down to the final 6 designers and I just wanted to take a moment and provide a bit of feedback regarding the concepts that we like and the modifications we are looking for. First, let me mention some of the design functions we like. - At the top of the homepage we really like the "region" or "language" tab so that the website can be viewed in both English and Arabic. - We like the homepage to have clear color variation so that the different sections of the homepage are distinct. Additionally, we like the bottom portion of the homepage to be in red. We feel that draws attention to our contact information. Again, we would like the colors to integrate black, gray-scale, red, etc. - Having a search tab at the top of the home page, or integrated into the main image, so that the site is easy to navigate. - We especially like the main image to have the scrolling tabs at the bottom so it is easy to browse the services offered (Consultancy, Solutions Architecture, Masters Systems Integration, Independent Design Review). - In regards to the services offered tab we really like the idea that a few people presented that have the outside of our logo with an icon in the middle of consultancy, solutions, etc., etc. Secondly, as mentioned in our brief we really enjoy the design of vortrane site. Specially, we enjoy the strong iconic images they use, the way the tabs at the top scroll easily, and contact us page that generates an email. Lastly, I've included some photos of the concept we have been working on. What we are trying to demonstrate is how our company offers a range of services that are essentially linked together. We provide individual services that when combined present the full service package. We would like this concept to be integrated into the over concept of our website. Please feel free to ask for clarification of any of the above points or contact us if you have any additional questions. We appreciate all of your hard work and are very excited to see the updated designs. Best, Miriam Dowbrook Plenvaro Senior Program Manager miriam.dowbrook@plenvaro-mail.com

Industry/Entity Type

Government

Font styles to use
Serif
Sans Serif

Requirements
Must have
• Must work on/adapt to various/mobile devices (responsive)
Must be simple and straightforward
Colors should be in line/matching with logo
2 language versions: English and Arabic (no Thai)
Services should be the first group/row of items after/below the main image
Note: the website will be hosted by hostpeak
Nice to have
• Submit feedback form
What's New section
The banner at the bottom of the site should not be too large; we would like a narrow one more
It would be nice if the header/top banner (with Home, About, etc. tabs) could stay in place as you scroll down (like Vortrane and Chatterly)
We will likely only use one image with a Company slogan on the Home page rather than a carousel of images to rotate through
Should not have
• This is the existing website: http://www.plenvaro-example.org
We do not like the animation, the way the banner icons/titles bounce
Not simple enough, we don't like the functionality or how pages load so slowly
We do not like the logo centered - it should be at the left
The banner and its tabs should not be towards the right, we would like them to be centered, to go all the way across and to be below the logo

```html
<!DOCTYPE html>
<html lang="en">
<head>
<meta charset="utf-8">
<title>Plenvaro – Systems and Technology Consultants</title>
<link href="https://fonts.googleapis.com/css2?family=Open+Sans:wght@400;600;700&display=swap" rel="stylesheet">
<style>
:root{
  --red:#d7141d;
  --red-dark:#b80f17;
  --ink:#222;
  --muted:#666;
  --line:#ddd;
  --band:#efefef;
  --footer:#f2f2f2;
  --footer-bar:#e6e6e6;
  --white:#fff;
}
*{box-sizing:border-box;margin:0;padding:0}
html,body{width:706px;height:1200px;overflow:hidden;background:var(--white)}
body{font-family:"Open Sans",Arial,sans-serif;color:var(--ink);position:relative}
.abs{position:absolute}

/* header */
.brand{left:72px;top:22px;display:flex;align-items:center;gap:10px}
.brand-mark{width:30px;height:30px;background:var(--red)}
.brand-name{font-size:28px;font-weight:700;color:var(--red);letter-spacing:2px}
.top-social{right:70px;top:20px;display:flex;gap:6px}
.top-social span{width:13px;height:13px;border-radius:50%;background:#bbb;display:block}
.search{right:70px;top:42px;width:126px;height:16px;border:1px solid #ccc;font-size:8px;color:#999;padding:2px 6px;display:flex;justify-content:space-between;align-items:center}

/* nav */
.main-nav{left:0;top:82px;width:706px;height:20px;background:var(--red)}
.main-nav ul{list-style:none;display:flex;margin-left:86px;height:100%}
.main-nav li{font-size:9px;color:var(--white);padding:0 17px;line-height:20px}
.main-nav li.active{background:#111}
.main-nav li:nth-child(2){margin-left:12px}

/* hero */
.hero{left:0;top:102px;width:706px;height:227px;background:linear-gradient(100deg,#dfe7ea 0%,#c9dbe2 45%,#a8c6d2 100%)}
.hero-photo{right:70px;top:0;width:190px;height:227px;background:linear-gradient(180deg,#e9eef0,#c3d3d9)}
.hero-title{left:72px;top:163px;background:rgba(255,255,255,.85);padding:2px 10px;font-size:22px;color:#333}
.hero-title b{color:var(--red)}
.hero-text{left:72px;top:196px;width:310px;font-size:8px;line-height:11px;color:#333;background:rgba(255,255,255,.6);padding:2px 4px}
.btn{background:var(--red);color:var(--white);font-size:10px;text-align:center}
.hero-btn{left:72px;top:229px;width:64px;height:18px;line-height:18px;border-radius:2px}

/* services */
.service{top:350px;width:130px;text-align:center}
.service-photo{height:120px;background:linear-gradient(160deg,#7c8ea3,#3d5670)}
.service-title{font-size:9px;font-weight:700;margin-top:14px}
.service-text{font-size:7px;line-height:10px;color:var(--muted);margin-top:4px;padding:0 4px}
.service-icon{width:14px;height:14px;border-radius:50%;background:var(--red);margin:14px auto 0}

/* news band */
.news-band{left:0;top:614px;width:706px;height:198px;background:var(--band)}
.section-title{font-size:17px;color:#222}
.news-item{left:66px;width:360px;display:flex;gap:10px}
.news-photo{width:80px;height:38px;background:linear-gradient(160deg,#a9b7c3,#5c7286);flex:none}
.news-text{font-size:7px;line-height:10px;color:#444}
.video{left:447px;top:658px;width:194px;height:130px;background:linear-gradient(160deg,#1a3a5a,#0b1d33)}
.video-bar{left:447px;top:776px;width:194px;height:12px;background:#000;opacity:.7}

/* newsletter */
.newsletter-title{left:0;top:848px;width:706px;text-align:center;font-size:14px;font-weight:700}
.newsletter-text{left:150px;top:876px;width:406px;text-align:center;font-size:8px;line-height:11px;color:#333}
.newsletter-input{left:153px;top:930px;width:295px;height:22px;border:1px solid var(--line);font-size:7px;color:#999;padding:6px 10px}
.newsletter-btn{left:458px;top:930px;width:98px;height:22px;line-height:22px;border-radius:2px}

/* footer */
.footer{left:0;top:985px;width:706px;height:182px;background:var(--footer)}
.footer-col{top:1002px}
.footer-col h4{font-size:13px;font-weight:400;color:#444;margin-bottom:8px}
.footer-col p{font-size:7px;line-height:17px;color:#555}
.foot-social{left:515px;top:1063px;display:flex;gap:8px}
.foot-social span{width:18px;height:18px;border-radius:50%;border:1px solid #bbb;display:block}
.footer-bar{left:0;top:1167px;width:706px;height:33px;background:var(--footer-bar);font-size:8px;color:#444}
.copyright{left:75px;top:12px}
.legal{right:70px;top:12px;display:flex;gap:20px}
</style>
</head>
<body>

<header>
  <div class="abs brand"><span class="brand-mark"></span><span class="brand-name">PLENVARO</span></div>
  <div class="abs top-social"><span></span><span></span><span></span><span></span></div>
  <div class="abs search">Search
    <svg width="8" height="8" viewBox="0 0 10 10"><circle cx="4" cy="4" r="3" fill="none" stroke="#888" stroke-width="1.2"/><line x1="6.3" y1="6.3" x2="9.5" y2="9.5" stroke="#888" stroke-width="1.2"/></svg>
  </div>
</header>

<nav class="abs main-nav">
  <ul>
    <li class="active">Home</li><li>Business Units</li><li>Services</li><li>About Us</li><li>Locations</li><li>Contact Us</li>
  </ul>
</nav>

<section class="abs hero">
  <div class="abs hero-photo" role="img" aria-label="Photo of a consultant with technology graphics"></div>
</section>
<h1 class="abs hero-title">Welcome To <b>PLENVARO TECHNIC</b></h1>
<p class="abs hero-text">Lorem ipsum dolor sit amet, consectetuer adipiscing elit, sed diam nonummy nibh euismod tincidunt ut laoreet dolore magna aliquam erat volutpat.</p>
<div class="abs btn hero-btn">Read More</div>

<section>
  <div class="abs service" style="left:78px">
    <div class="service-photo" role="img" aria-label="Photo of a business meeting"></div>
    <h3 class="service-title">CONSULTING</h3>
    <p class="service-text">Lorem ipsum dolor sit amet, con sectetuer adipiscing elit, sed diam nonummy nibh euismod tincidunt ut laoreet dolore magna aliquam erat volutpat.</p>
    <div class="service-icon"></div>
  </div>
  <div class="abs service" style="left:223px">
    <div class="service-photo" role="img" aria-label="Photo of office buildings"></div>
    <h3 class="service-title">ENGINEERING</h3>
    <p class="service-text">Lorem ipsum dolor sit amet, con sectetuer adipiscing elit, sed diam nonummy nibh euismod tincidunt ut laoreet dolore magna aliquam erat volutpat.</p>
    <div class="service-icon"></div>
  </div>
  <div class="abs service" style="left:364px">
    <div class="service-photo" role="img" aria-label="Photo of a construction team on site"></div>
    <h3 class="service-title">CONSTRUCTION</h3>
    <p class="service-text">Lorem ipsum dolor sit amet, con sectetuer adipiscing elit, sed diam nonummy nibh euismod tincidunt ut laoreet dolore magna aliquam erat volutpat.</p>
    <div class="service-icon"></div>
  </div>
  <div class="abs service" style="left:510px">
    <div class="service-photo" role="img" aria-label="Photo of a maintenance engineer in a hard hat"></div>
    <h3 class="service-title">MAINTANANCE</h3>
    <p class="service-text">Lorem ipsum dolor sit amet, con sectetuer adipiscing elit, sed diam nonummy nibh euismod tincidunt ut laoreet dolore magna aliquam erat volutpat.</p>
    <div class="service-icon"></div>
  </div>
</section>

<section class="abs news-band"></section>
<h2 class="abs section-title" style="left:66px;top:628px">Latest News</h2>
<div class="abs news-item" style="top:670px">
  <div class="news-photo" role="img" aria-label="Photo of colleagues at work"></div>
  <p class="news-text">Lorem ipsum dolor sit amet, consectetuer adipiscing elit, sed diam nonummy nibh euismod tincidunt ut laoreet dolore magna aliquam erat volutpat.</p>
</div>
<div class="abs news-item" style="top:742px">
  <div class="news-photo" role="img" aria-label="Photo of a team meeting"></div>
  <p class="news-text">Lorem ipsum dolor sit amet, consectetuer adipiscing elit, sed diam nonummy nibh euismod tincidunt ut laoreet dolore magna aliquam erat volutpat.</p>
</div>
<h2 class="abs section-title" style="left:447px;top:628px">Featured Video</h2>
<div class="abs video" role="img" aria-label="Featured video still with technology graphics">
  <svg class="abs" style="left:80px;top:45px" width="34" height="26" viewBox="0 0 34 26"><rect width="34" height="26" rx="4" fill="#000" opacity=".6"/><polygon points="13,7 23,13 13,19" fill="#fff"/></svg>
</div>
<div class="abs video-bar"></div>

<section>
  <h2 class="abs newsletter-title">Subscribe Our Newsletter</h2>
  <p class="abs newsletter-text">Lorem ipsum dolor sit amet, consectetuer adipiscing elit, sed diam nonummy nibh euismod tincidunt ut laoreet dolore magna aliquam erat volutpat.</p>
  <div class="abs newsletter-input">Enter Email Address</div>
  <div class="abs btn newsletter-btn">Subscribe</div>
</section>

<footer>
  <div class="abs footer"></div>
  <div class="abs footer-col" style="left:75px"><h4>Info</h4><p>Sign Up Now<br>Free Trail<br>Features<br>Try it Now</p></div>
  <div class="abs footer-col" style="left:174px"><h4>Email</h4><p>info@plenvaro-mail.com</p></div>
  <div class="abs footer-col" style="left:277px"><h4>Company</h4><p>Careers</p></div>
  <div class="abs footer-col" style="left:388px"><h4>Contact Us</h4><p>Lorem ipsum dolor sit amet<br>Consectetuer<br>Adipiscing<br>Elit Sed Do<br>Call Us: 0123 456 7890</p></div>
  <div class="abs foot-social"><span></span><span></span><span></span><span></span></div>
  <div class="abs footer-bar">
    <span class="abs copyright">Copyright2014. All Right Reserved</span>
    <span class="abs legal"><span>Privacy Policy</span><span>Terms and Conditions</span></span>
  </div>
</footer>

</body>
</html>
```